Business Cards for Communications Technology Company

We are an innovative software company based in Tropical North Queensland, Australia. We have several brands with a focus on communications software for businesses. We are looking for a business card that is very innovate and creative whilst still remaining professional on a corporate level.

Our internal culture is very progressive and expresses a blend between the clarity of our natural surroundings and the highly technological industry we work in. Our current branding blends a modern minimalist typeface with the desire to push the boundaries in the way we communicate.

This is a corporate level business card for the communications software industry and may possibly also encompass our brands MarNetwork, PelFax, TukMailer and our B2B marketing service—with our companies name being Viresca Partners. Showing other brands on the business card is optional not compulsory.

Technical notes:

-We will attach all logo's and some examples of our corporate branding
- Would be willing to print with various papers, embossed, metallic ink, curved edges etc. in a standard business card size

Sample content:

Rowan Pellick
Senior Account Manager
Phone: 1300 842 916 / +617 4583 2764
Email: r.pellick@viresca.com.au
Web: www.viresca.com.au

Sincerely,
Viresca Partners.

```html
<!DOCTYPE html>
<html lang="en">
<head>
<meta charset="utf-8">
<title>Viresca Partners – Business Card</title>
<link rel="stylesheet" href="https://fonts.googleapis.com/css2?family=Roboto:wght@400;500&display=swap">
<style>
  :root {
    --backdrop: #5c5d5f;
    --card: #1b2220;
    --silver: #b9bdbf;
    --muted: #a9adab;
    --white: #f1f3f2;
    --green: #6cb33f;
    --orange: #e07b2e;
    --blue: #1d86d0;
    --rule: #8d9290;
  }
  * { box-sizing: border-box; margin: 0; padding: 0; }
  html, body { width: 1200px; height: 1200px; overflow: hidden; }
  body {
    background: var(--backdrop);
    font-family: "Roboto", Arial, sans-serif;
    display: flex;
    flex-direction: column;
    align-items: center;
    justify-content: center;
    gap: 70px;
  }
  .card {
    position: relative;
    width: 760px;
    height: 440px;
    background: var(--card);
    box-shadow: 0 6px 18px rgba(0,0,0,.35);
  }
  .brand-mark {
    display: flex;
    align-items: center;
    gap: 14px;
    color: var(--silver);
    font-weight: 500;
    letter-spacing: .02em;
  }
  .brand-mark .dot {
    border-radius: 50%;
    background: var(--silver);
    flex: none;
  }
  .card-front .brand-mark {
    position: absolute;
    left: 70px;
    top: 130px;
    font-size: 36px;
    line-height: 1.05;
    width: 280px;
  }
  .divider {
    position: absolute;
    left: 372px;
    top: 40px;
    width: 3px;
    height: 190px;
    background: var(--rule);
  }
  .contact-block {
    position: absolute;
    left: 400px;
    top: 36px;
  }
  .person-name { color: var(--green); font-size: 27px; font-weight: 400; }
  .person-role { color: var(--muted); font-size: 21px; margin-top: 4px; }
  .contact-list { list-style: none; margin-top: 26px; }
  .contact-list li {
    display: flex;
    align-items: center;
    gap: 12px;
    color: var(--white);
    font-size: 21px;
    line-height: 30px;
  }
  .contact-list svg { width: 16px; height: 16px; fill: var(--white); flex: none; }
  .brand-family {
    position: absolute;
    left: 240px;
    top: 268px;
    display: flex;
    align-items: center;
  }
  .family-hub {
    width: 118px; height: 118px;
    border-radius: 50%;
    background: radial-gradient(circle at 40% 35%, #a4a8aa, #5b6062);
  }
  .family-link { width: 46px; height: 2px; background: var(--white); margin: 0 22px 0 12px; }
  .family-list { list-style: none; }
  .family-list li {
    display: flex; align-items: center; gap: 10px;
    font-size: 27px; font-weight: 500; line-height: 42px;
  }
  .family-list .dot { width: 16px; height: 16px; border-radius: 50%; }
  .fam-net { color: var(--orange); } .fam-net .dot { background: var(--orange); }
  .fam-fax { color: var(--green); } .fam-fax .dot { background: var(--green); }
  .fam-mail { color: var(--blue); } .fam-mail .dot { background: var(--blue); }
  .card-back { display: flex; align-items: center; justify-content: center; }
  .card-back .brand-mark { font-size: 52px; }
  .card-back .brand-mark .dot { width: 84px; height: 84px; }
</style>
</head>
<body>
  <section class="card card-front">
    <div class="brand-mark">Viresca Partners</div>
    <div class="divider"></div>
    <div class="contact-block">
      <p class="person-name">Rowan Pellick</p>
      <p class="person-role">Senior Account Manager</p>
      <ul class="contact-list">
        <li><svg viewBox="0 0 16 16"><path d="M4 0h8a1 1 0 0 1 1 1v14a1 1 0 0 1-1 1H4a1 1 0 0 1-1-1V1a1 1 0 0 1 1-1zm1 2v10h6V2z"/></svg>1300 842 916</li>
        <li><svg viewBox="0 0 16 16"><path d="M3 1l3 3-1.5 2a9 9 0 0 0 5.5 5.5L12 10l3 3-2 2C6 14 2 10 1 3z"/></svg>617 4583 2764</li>
        <li><svg viewBox="0 0 16 16"><path d="M1 3h14v10H1zm1 1.5v.5l6 4 6-4v-.5L8 8z"/></svg>r.pellick@viresca.com.au</li>
        <li><svg viewBox="0 0 16 16"><path d="M8 0a8 8 0 1 0 0 16A8 8 0 0 0 8 0zm0 1.5c.9 0 1.8 2 2 5.5H6c.2-3.5 1.1-5.5 2-5.5zM2 7h2.5c0-2 .4-3.6 1-4.6A6.5 6.5 0 0 0 2 7zm9.5 0H14a6.5 6.5 0 0 0-3.5-4.6c.6 1 1 2.6 1 4.6zM2 9a6.5 6.5 0 0 0 3.5 4.6c-.6-1-1-2.6-1-4.6zm4 0c.2 3.5 1.1 5.5 2 5.5s1.8-2 2-5.5zm5.5 0c0 2-.4 3.6-1 4.6A6.5 6.5 0 0 0 14 9z"/></svg>www.viresca.com.au</li>
      </ul>
    </div>
    <div class="brand-family">
      <div class="family-hub"></div>
      <div class="family-link"></div>
      <ul class="family-list">
        <li class="fam-net">MarNetwork <span class="dot"></span></li>
        <li class="fam-fax">PelFax <span class="dot"></span></li>
        <li class="fam-mail">TukMailer <span class="dot"></span></li>
      </ul>
    </div>
  </section>
  <section class="card card-back">
    <div class="brand-mark"><span class="dot"></span>Viresca Partners</div>
  </section>
</body>
</html>
```